依頼詳細
PCとスマホデザインの両方納品をいただきますが、
まずはデザインイメージが確認しやすいPCページのみの提案をお願いします。
スマホページは当選者に納品時にお願いしたいと思います。
スマホサイズについて、カンバスサイズは横幅375pxで作成し、2倍の横幅750pxのサイズで書き出ししてください。
(Retinaディスプレイに対応するため)
スマホページ作成時は、メニューが展開した際のデザインもお願いします。
レスポンシブウェブデザインを意識したデザインでお願いします。

■サイトマップ
添付の画面遷移図をご確認ください。

■参考サイト
https://harbor-mend-crew.com/
https://www.qv-tm.co.jp/

■内容について
工場や倉庫の修繕・改修・増築などを専門とするサービスサイトになります。

■素材写真
画像データについては、フリー素材から流用して
イメージ画像に当て込んでください。
足りない場合は、一旦他のサイトの写真をサンプルとして
入れてください。(サンプルなどの表記をお願いします)
また、購入が必要な写真などを利用した場合、
価格とサイト名を教えてください。

また、Nimbrel Stockで定期契約をしていますので、
Nimbrel Stockの画像は使用できます。
デザイン時はカンプ画像をお入れいただきますようお願いします。

■ロゴについて
添付のロゴデータを使用してください。

■ワイヤーフレーム
https://mk.velquora.com/view/600e5e1a-e3bd-4b32-a74b-244a4501d661-355d/?fullscreen
コンテンツの構成としてワイヤーフレームを作成しましたが
必ずしもワイヤーフレームの通りではなくて大丈夫です。
TOPページに配置するコンテンツを見ていただき、デザインは
デザイナーの皆様におまかせしたいと思います。

----------------------------------------------------------------------------
【制作物に対するお願い】

■フォントについて
・無料で使えるフォントで作成をお願いします。
・OSに紐づくフォントの使用は控えていただければと思います (ヒラギノなど)

サイトURL
ページ数
1ページ
希望イメージ
シンプル 複雑
単色 カラフル
暗い 明るい
日常 高級
遊び心 厳粛
未来的 伝統的
女性的 男性的
希望する色
ベースカラー:白、ポイントカラー:赤、青(救急のイメージ)
納品ファイル
• 高解像度JPG (.jpg)
• イラストレーター形式 (.ai)
• フォトショップ形式 (.psd)
補足説明
上記のいずれか1つ(アウトラインありとなしの2つ)と高解像度JPGを納品お願いします。
adobe XDでの納品も可能です。

```html
<!DOCTYPE html>
<html lang="ja">
<head>
<meta charset="utf-8">
<title>工場修繕レスキュー | 工場専門修繕サービス</title>
<link href="https://fonts.googleapis.com/css2?family=Noto+Sans+JP:wght@400;500;700;900&family=Oswald:wght@400;500&display=swap" rel="stylesheet">
<style>
:root{
  --red:#d7262c;
  --blue:#1a6fc4;
  --blue-dark:#135aa3;
  --ink:#222;
  --muted:#666;
  --line:#d9d9d9;
  --gray-bg:#f3f3f3;
  --white:#fff;
  --dark:#333;
}
*{box-sizing:border-box;margin:0;padding:0}
html,body{width:1200px;height:3640px;overflow:hidden}
body{font-family:"Noto Sans JP",sans-serif;color:var(--ink);background:var(--white);position:relative;font-size:13px}
.en{font-family:"Oswald",sans-serif;letter-spacing:.08em}
.photo{display:block}
/* header */
.site-header{position:absolute;top:0;left:0;width:1200px;height:80px;display:flex;align-items:center;padding-left:24px;background:var(--white)}
.brand{display:flex;align-items:center;gap:10px;font-weight:900;font-size:22px;color:var(--blue)}
.brand-mark{width:22px;height:22px;border-radius:50%;background:var(--red)}
.global-nav{margin-left:auto;display:flex;flex-direction:column;align-items:flex-end;gap:10px;margin-right:18px}
.header-tel{display:flex;align-items:center;gap:6px;font-family:"Oswald",sans-serif;font-size:20px;font-weight:500}
.global-nav ul{display:flex;gap:22px;list-style:none;font-size:12px;font-weight:500}
.header-cta{display:flex;height:80px}
.header-cta a{width:80px;display:flex;flex-direction:column;align-items:center;justify-content:center;gap:6px;color:var(--white);text-decoration:none;font-size:11px;font-weight:700;line-height:1.3;text-align:center}
.cta-contact{background:var(--blue)}
.cta-download{background:var(--red)}
/* hero */
.hero{position:absolute;top:80px;left:0;width:1200px;height:480px}
.hero-photo{position:absolute;inset:0;background:linear-gradient(160deg,#8e9aa6 0%,#4a5560 45%,#2a3036 100%)}
.hero-title{position:absolute;left:0;right:0;top:200px;text-align:center;color:var(--white)}
.hero-title h1{font-size:48px;font-weight:700;letter-spacing:.08em}
.hero-title p{font-size:14px;margin-top:4px}
/* feature */
.feature{position:absolute;top:620px;left:0;width:1200px;height:480px}
.feature-photo-left{position:absolute;left:0;top:0;width:360px;height:300px;background:linear-gradient(180deg,#c7a36f,#6b5a44 60%,#3e3a36)}
.feature-photo-right{position:absolute;right:0;top:150px;width:330px;height:300px;background:linear-gradient(180deg,#8fb2cf,#3c5a78 55%,#1f2c3b)}
.feature-body{position:absolute;left:410px;top:20px;width:420px;font-size:12px;line-height:2;color:var(--muted)}
.feature-body p+p{margin-top:20px}
.btn{display:inline-flex;align-items:center;justify-content:space-between;border:1px solid var(--ink);background:var(--white);font-family:"Oswald",sans-serif;font-size:11px;letter-spacing:.08em;padding:0 14px;height:40px;width:200px}
.feature .btn{margin-top:30px;margin-left:0}
/* section headings */
.sec-head h2{font-size:34px;font-weight:700;line-height:1.2}
.sec-head span{display:block;font-family:"Oswald",sans-serif;font-size:11px;letter-spacing:.1em;color:var(--blue);margin-top:4px;padding-bottom:4px;border-bottom:2px solid var(--blue);width:max-content}
/* works */
.works{position:absolute;top:1160px;left:0;width:1200px;height:520px;background:var(--gray-bg)}
.works .sec-head{position:absolute;left:225px;top:70px}
.works .btn{position:absolute;right:225px;top:86px;width:170px}
.works-track{position:absolute;top:170px;left:-110px;display:flex;gap:30px}
.work-card{width:210px}
.work-card .photo{height:180px}
.work-meta{font-size:10px;color:var(--muted);margin-top:12px}
.work-title{font-size:12px;font-weight:500;margin-top:4px}
.work-foot{display:flex;justify-content:space-between;align-items:center;margin-top:12px}
.work-foot .tag{font-size:10px;color:var(--muted)}
.work-foot .mini{border:1px solid var(--ink);background:var(--white);font-family:"Oswald",sans-serif;font-size:9px;padding:4px 10px}
.arrow-btn{position:absolute;top:240px;width:40px;height:40px;border-radius:50%;background:var(--dark);display:flex;align-items:center;justify-content:center}
/* column */
.column{position:absolute;top:1740px;left:0;width:1200px;height:600px}
.column .sec-head{position:absolute;left:225px;top:50px}
.column .btn{position:absolute;right:225px;top:66px;width:170px}
.col-main{position:absolute;left:225px;top:150px;width:340px;height:410px;background:var(--white);box-shadow:0 2px 10px rgba(0,0,0,.12)}
.col-main .photo{height:250px;background:linear-gradient(170deg,#c9b690,#7b6a53 55%,#3f3428)}
.col-text{padding:16px 18px;font-size:11px;line-height:1.8}
.col-text .date{color:var(--muted);font-size:10px}
.col-text .title{font-weight:700;font-size:13px;margin:4px 0 8px}
.col-text .desc{color:var(--muted)}
.col-sub{position:absolute;left:600px;width:375px;height:195px;background:var(--white);box-shadow:0 2px 10px rgba(0,0,0,.12);display:flex}
.col-sub .photo{width:165px;height:100%}
.col-sub .col-text{flex:1;padding:28px 16px}
/* news */
.news{position:absolute;top:2370px;left:0;width:1200px;height:400px;background:var(--gray-bg)}
.news .sec-head{position:absolute;left:225px;top:60px}
.news .btn{position:absolute;left:225px;top:180px;width:170px}
.news-list{position:absolute;left:450px;top:50px;width:525px;list-style:none}
.news-list li{display:flex;gap:24px;padding:16px 0;border-bottom:1px solid var(--line);font-size:11px;line-height:1.7}
.news-list time{color:var(--muted);font-family:"Oswald",sans-serif;flex:none;width:70px}
/* contents */
.contents{position:absolute;top:2770px;left:0;width:1200px;height:560px}
.contents-band{position:absolute;left:0;right:0;top:240px;bottom:0;background:var(--blue)}
.contents .sec-head{position:absolute;left:225px;top:40px}
.contents-list{position:absolute;left:225px;top:130px;display:flex;gap:20px}
.content-card{position:relative;width:237px;height:210px;color:var(--white)}
.content-card .photo{position:absolute;inset:0}
.content-label{position:absolute;left:16px;bottom:16px}
.content-label small{display:block;font-family:"Oswald",sans-serif;font-size:10px;letter-spacing:.08em}
.content-label strong{font-size:15px;font-weight:700}
.contact-head{position:absolute;left:225px;top:385px;color:var(--white)}
.contact-head h2{font-size:30px;font-weight:700}
.contact-head span{font-family:"Oswald",sans-serif;font-size:11px;letter-spacing:.1em}
.contact-head p{font-size:11px;margin-top:16px;line-height:1.7}
.contact-tel{position:absolute;left:450px;top:385px;width:250px;height:110px;border:1px solid var(--white);color:var(--white);text-align:center;padding-top:18px}
.contact-tel small{font-size:10px}
.contact-tel strong{display:block;font-family:"Oswald",sans-serif;font-size:30px;font-weight:500;line-height:1.3}
.contact-tel .note{display:inline-block;background:var(--white);color:var(--blue);font-size:10px;padding:2px 10px;margin-top:4px}
.contact-mail{position:absolute;left:725px;top:385px;width:250px;height:110px;background:var(--white);display:flex;flex-direction:column;align-items:center;justify-content:center;gap:8px;color:var(--blue);font-size:12px;font-weight:700}
/* footer */
.site-footer{position:absolute;top:3330px;left:0;width:1200px;height:310px;background:var(--white)}
.footer-brand{position:absolute;left:225px;top:40px}
.footer-brand .brand{font-size:20px}
.footer-tel{margin-top:14px;font-family:"Oswald",sans-serif;font-size:20px;display:flex;align-items:center;gap:6px}
.footer-brand p{font-size:10px;color:var(--muted);margin-top:10px;line-height:1.8}
.footer-nav{position:absolute;top:40px;display:flex;flex-direction:column;gap:9px;list-style:none;font-size:11px}
.footer-nav li.head{font-weight:700}
.copyright{position:absolute;left:0;right:0;bottom:40px;text-align:center;font-size:10px;color:var(--muted)}
.to-top{position:absolute;right:20px;bottom:20px;width:40px;height:40px;background:var(--ink);display:flex;align-items:center;justify-content:center}
</style>
</head>
<body>

<header class="site-header">
  <div class="brand"><span class="brand-mark"></span>工場修繕レスキュー</div>
  <nav class="global-nav">
    <div class="header-tel">
      <svg width="16" height="16" viewBox="0 0 24 24"><path fill="#222" d="M6.6 10.8a15.1 15.1 0 0 0 6.6 6.6l2.2-2.2c.3-.3.7-.4 1-.2 1.1.4 2.3.6 3.6.6.6 0 1 .4 1 1V20c0 .6-.4 1-1 1A17 17 0 0 1 3 4c0-.6.4-1 1-1h3.5c.6 0 1 .4 1 1 0 1.3.2 2.5.6 3.6.1.3 0 .7-.2 1z"/></svg>
      0120-48-7731
    </div>
    <ul>
      <li>ホーム</li><li>工場修繕レスキューの特徴</li><li>サービス一覧</li><li>施工実績</li><li>会社概要</li><li>よくあるご質問</li>
    </ul>
  </nav>
  <div class="header-cta">
    <a class="cta-contact" href="#contact">
      <svg width="20" height="14" viewBox="0 0 20 14"><rect x="1" y="1" width="18" height="12" fill="none" stroke="#fff" stroke-width="1.5"/><path d="M1 1l9 7 9-7" fill="none" stroke="#fff" stroke-width="1.5"/></svg>
      お問い合わせ<br>はこちら</a>
    <a class="cta-download" href="#contents">
      <svg width="16" height="16" viewBox="0 0 16 16"><path d="M8 1v9M4 6l4 4 4-4M2 14h12" fill="none" stroke="#fff" stroke-width="1.6"/></svg>
      資料<br>ダウンロード</a>
  </div>
</header>

<section class="hero">
  <div class="hero-photo" role="img" aria-label="工場内で溶接作業を行う作業員の写真"></div>
  <div class="hero-title">
    <h1>工場専門修繕サービス</h1>
    <p class="en">FEATURE</p>
  </div>
</section>

<section class="feature">
  <div class="feature-photo-left" role="img" aria-label="照明が並ぶ大型工場内部の写真"></div>
  <div class="feature-body">
    <p>テキストテキストテキストテキストテキストテキストテキストテキストテキストテキストテキストテキストテキストテキストテキストテキストテキストテキストテキストテキストテキストテキストテキストテキストテキストテキストテキストテキストテキスト</p>
    <p>テキストテキストテキストテキストテキストテキストテキストテキストテキストテキストテキストテキストテキストテキストテキストテキストテキストテキストテキストテキストテキストテキストテキスト</p>
    <a class="btn">VIEW MORE
      <svg width="16" height="8" viewBox="0 0 16 8"><path d="M0 4h15M11 0l4 4-4 4" fill="none" stroke="#222"/></svg></a>
  </div>
  <div class="feature-photo-right" role="img" aria-label="照明に照らされた倉庫の床の写真"></div>
</section>

<section class="works">
  <div class="sec-head"><h2>施工実績</h2><span>WORKS</span></div>
  <a class="btn">VIEW ALL
    <svg width="16" height="8" viewBox="0 0 16 8"><path d="M0 4h15M11 0l4 4-4 4" fill="none" stroke="#222"/></svg></a>
  <div class="works-track">
    <article class="work-card"><div class="photo" role="img" aria-label="工場屋根の施工写真" style="background:linear-gradient(160deg,#a7b8c6,#55697a)"></div>
      <p class="work-meta">株式会社〇〇様</p><p class="work-title">工場屋根改修工事</p>
      <div class="work-foot"><span class="tag">屋根工事</span><span class="mini">VIEW MORE</span></div></article>
    <article class="work-card"><div class="photo" role="img" aria-label="鉄骨造の工場内部の写真" style="background:linear-gradient(160deg,#b9c9d6,#4f6f8c)"></div>
      <p class="work-meta">株式会社〇〇様</p><p class="work-title">工場増築工事</p>
      <div class="work-foot"><span class="tag">増築工事</span><span class="mini">VIEW MORE</span></div></article>
    <article class="work-card"><div class="photo" role="img" aria-label="倉庫の柱と照明の写真" style="background:linear-gradient(160deg,#7d8fa3,#2f4050)"></div>
      <p class="work-meta">株式会社〇〇様</p><p class="work-title">倉庫床改修工事</p>
      <div class="work-foot"><span class="tag">床工事</span><span class="mini">VIEW MORE</span></div></article>
    <article class="work-card"><div class="photo" role="img" aria-label="倉庫の棚と作業員の写真" style="background:linear-gradient(160deg,#c9a874,#6a5a45)"></div>
      <p class="work-meta">株式会社〇〇様</p><p class="work-title">倉庫内装工事</p>
      <div class="work-foot"><span class="tag">内装工事</span><span class="mini">VIEW MORE</span></div></article>
    <article class="work-card"><div class="photo" role="img" aria-label="新築の工場外観の写真" style="background:linear-gradient(180deg,#9fc3e3,#8d9aa5 60%,#5d6670)"></div>
      <p class="work-meta">株式会社〇〇様</p><p class="work-title">工場外壁改修工事</p>
      <div class="work-foot"><span class="tag">外壁工事</span><span class="mini">VIEW MORE</span></div></article>
    <article class="work-card"><div class="photo" role="img" aria-label="工場内部の設備の写真" style="background:linear-gradient(160deg,#a0b4c7,#3f5a73)"></div>
      <p class="work-meta">株式会社〇〇様</p><p class="work-title">設備更新工事</p>
      <div class="work-foot"><span class="tag">設備工事</span><span class="mini">VIEW MORE</span></div></article>
  </div>
  <span class="arrow-btn" style="left:80px"><svg width="12" height="12" viewBox="0 0 12 12"><path d="M8 1L3 6l5 5" fill="none" stroke="#fff" stroke-width="1.6"/></svg></span>
  <span class="arrow-btn" style="right:80px"><svg width="12" height="12" viewBox="0 0 12 12"><path d="M4 1l5 5-5 5" fill="none" stroke="#fff" stroke-width="1.6"/></svg></span>
</section>

<section class="column">
  <div class="sec-head"><h2>コラム</h2><span>COLUMN</span></div>
  <a class="btn">VIEW ALL
    <svg width="16" height="8" viewBox="0 0 16 8"><path d="M0 4h15M11 0l4 4-4 4" fill="none" stroke="#222"/></svg></a>
  <article class="col-main">
    <div class="photo" role="img" aria-label="建設現場を見渡す作業員の後ろ姿の写真"></div>
    <div class="col-text"><p class="date en">2024.00.00</p>
      <p class="title">タイトルタイトルタイトルタイトルタイトルタイトルタイトル</p>
      <p class="desc">テキストテキストテキストテキストテキストテキストテキストテキストテキストテキスト</p></div>
  </article>
  <article class="col-sub" style="top:150px">
    <div class="photo" role="img" aria-label="鉄骨の骨組みの写真" style="background:linear-gradient(180deg,#a9cbe8,#6f8fa9)"></div>
    <div class="col-text"><p class="date en">2024.00.00</p>
      <p class="title">タイトルタイトルタイトルタイトルタイトルタイトル</p>
      <p class="desc">テキストテキストテキスト</p></div>
  </article>
  <article class="col-sub" style="top:365px">
    <div class="photo" role="img" aria-label="現場で作業する作業員の写真" style="background:linear-gradient(170deg,#b7c2cb,#55626e)"></div>
    <div class="col-text"><p class="date en">2024.00.00</p>
      <p class="title">タイトルタイトルタイトルタイトルタイトルタイトル</p>
      <p class="desc">テキストテキストテキスト</p></div>
  </article>
</section>

<section class="news">
  <div class="sec-head"><h2>お知らせ</h2><span>NEWS</span></div>
  <a class="btn">VIEW ALL
    <svg width="16" height="8" viewBox="0 0 16 8"><path d="M0 4h15M11 0l4 4-4 4" fill="none" stroke="#222"/></svg></a>
  <ul class="news-list">
    <li><time>2024.00.00</time><span>お知らせのタイトルが入ります。お知らせのタイトルが入ります。お知らせのタイトル</span></li>
    <li><time>2024.00.00</time><span>お知らせのタイトルが入ります。お知らせのタイトルが入ります。</span></li>
    <li><time>2024.00.00</time><span>お知らせのタイトルが入ります。お知らせのタイトルが入ります。お知らせのタイトル</span></li>
    <li><time>2024.00.00</time><span>お知らせのタイトルが入ります。</span></li>
    <li><time>2024.00.00</time><span>お知らせのタイトルが入ります。お知らせのタイトルが入ります。</span></li>
  </ul>
</section>

<section class="contents" id="contents">
  <div class="contents-band"></div>
  <div class="sec-head"><h2>コンテンツ</h2><span>CONTENTS</span></div>
  <div class="contents-list">
    <a class="content-card"><div class="photo" role="img" aria-label="ヘルメットを被った作業員の写真" style="background:linear-gradient(170deg,#6d7f90,#24303b)"></div>
      <div class="content-label"><small>FAQ</small><strong>よくあるご質問</strong></div></a>
    <a class="content-card"><div class="photo" role="img" aria-label="打ち合わせをする作業員の写真" style="background:linear-gradient(170deg,#8a7d6c,#2e2a26)"></div>
      <div class="content-label"><small>FLOW</small><strong>お問い合わせの流れ</strong></div></a>
    <a class="content-card"><div class="photo" role="img" aria-label="図面と資料の写真" style="background:linear-gradient(170deg,#9ba7b2,#3b4650)"></div>
      <div class="content-label"><small>DOWNLOAD</small><strong>カタログダウンロード</strong></div></a>
  </div>
  <div class="contact-head" id="contact">
    <h2>お問い合わせ</h2><span>CONTACT</span>
    <p>工場修繕のご相談は<br>お気軽にお問い合わせください</p>
  </div>
  <div class="contact-tel">
    <small>受付時間 9:00〜18:00（土日祝除く）</small>
    <strong>0120-48-7731</strong>
    <span class="note">工場修繕レスキューを見たとお伝えください</span>
  </div>
  <a class="contact-mail">
    <svg width="28" height="20" viewBox="0 0 28 20"><rect x="1" y="1" width="26" height="18" fill="none" stroke="#1a6fc4" stroke-width="1.8"/><path d="M1 1l13 10L27 1" fill="none" stroke="#1a6fc4" stroke-width="1.8"/></svg>
    メールフォームはこちら
  </a>
</section>

<footer class="site-footer">
  <div class="footer-brand">
    <div class="brand"><span class="brand-mark"></span>工場修繕レスキュー</div>
    <div class="footer-tel">
      <svg width="16" height="16" viewBox="0 0 24 24"><path fill="#222" d="M6.6 10.8a15.1 15.1 0 0 0 6.6 6.6l2.2-2.2c.3-.3.7-.4 1-.2 1.1.4 2.3.6 3.6.6.6 0 1 .4 1 1V20c0 .6-.4 1-1 1A17 17 0 0 1 3 4c0-.6.4-1 1-1h3.5c.6 0 1 .4 1 1 0 1.3.2 2.5.6 3.6.1.3 0 .7-.2 1z"/></svg>
      0120-48-7731</div>
    <p>プライバシーポリシー</p>
  </div>
  <ul class="footer-nav" style="left:560px">
    <li class="head">ホーム</li><li>工場修繕レスキューの特徴</li><li>施工実績</li><li>コラム</li><li>お知らせ</li>
  </ul>
  <ul class="footer-nav" style="left:730px">
    <li class="head">サービス一覧</li><li>屋根工事</li><li>外壁工事</li><li>床工事</li><li>増築工事</li>
  </ul>
  <ul class="footer-nav" style="left:860px">
    <li class="head">会社概要</li><li>よくあるご質問</li><li>お問い合わせの流れ</li><li>カタログダウンロード</li><li>お問い合わせ</li>
  </ul>
  <p class="copyright">Copyright © 工場修繕レスキュー All Rights Reserved.</p>
  <a class="to-top"><svg width="12" height="12" viewBox="0 0 12 12"><path d="M1 8l5-5 5 5" fill="none" stroke="#fff" stroke-width="1.6"/></svg></a>
</footer>

</body>
</html>
```